Design Clipwerk B2B-Website
Zielgruppe
Das entstehende Portal bietet Videos zum Streaming an und richtet sich an Geschäftskunden, stellt also einen Shop mit Login dar. Das Angebot der Videos ist offen einsehbar, das Streamen ist gegen Bezahlung im Shop zu erwerben.
Aufgabenstellung
Die Seite soll sich im Layout an brevoqueue.com orientieren; das Farbschema angelehnt an folgende
Hexcodes:
#231f20, #60bb46 und #828282 (und ähnliche Töne). Sprache ist Deutsch.
1. Startseite/Allgemein
Die dortige Navigationsleiste oben soll etwas größer werden; wird erweitert duch ein Logo links (muss NICHT designt werden; bitte mit Platzhalter füllen); die Navigationsitems (Angebot, Preise, Über uns, FAQ, Blog), mit Farb-hover-Effekt, sollen eine Kombination aus kleine Icon und Text sein; auf der rechten Seite die Buttons "Anmelden" (nicht rot), "Login" und Suchfenster mit Lupe und "Suche". Ein Zusatzmenü wie beim Klick auf "More"
soll mitdesigned werden (Items können Platzhalter sein).
Im Hauptteil eine Box mit Auflistung von Videos (auch zum Ansehen).
Die Seite enthält ebenso einen deutlichen Footer (umfangreicher).
2. Unterseite
Inhalt der Unterseite kann beispielhaft von "Features" bzw. "Pricing" entnommen werden. Dazu hell-grauer Hintergrund (verlaufend), mit eingepassten Bildern.
"Login"-Fenster bzw. "Anmelden" ähnlich zu Brevoqueue; mehr Felder und Farbschema siehe oben.
3.Login-Bereich
Im Login-Bereich (sprich wenn der Nutzer eingeloggt ist), soll die Navigation (mit anderen Items) nach links wandern und vertikal angeordnet werden. Im Hauptinhalt(rechts von der Navigation) sollen dann die Videos oder anderen Inhalte dargestellt werden.

```html
<!DOCTYPE html>
<html lang="de">
<head>
<meta charset="utf-8">
<title>Clipwerk B2B – Angebot</title>
<link rel="stylesheet" href="https://fonts.googleapis.com/css2?family=Open+Sans:wght@400;600;700&family=Oswald:wght@400&display=swap">
<style>
  :root {
    --ink: #231f20;
    --bar: #262626;
    --green: #60bb46;
    --grey: #828282;
    --page: #ececec;
    --footer: #808080;
    --star-off: #d2d2d2;
  }
  * { box-sizing: border-box; margin: 0; padding: 0; }
  html, body { width: 976px; height: 1200px; overflow: hidden; }
  body {
    position: relative;
    background: var(--page);
    font-family: "Open Sans", Arial, sans-serif;
    color: var(--ink);
  }

  .site-header { position: absolute; left: 0; top: 0; width: 976px; height: 78px; }
  .brand {
    position: absolute; left: 185px; top: 18px;
    display: flex; align-items: center; gap: 8px;
    font-size: 24px; font-weight: 700; color: var(--ink);
  }
  .brand-mark { width: 22px; height: 22px; background: var(--green); }
  .btn-register {
    position: absolute; left: 667px; top: 0; width: 66px; height: 30px;
    background: var(--green); color: #fff; font-size: 11px; font-weight: 600;
    display: flex; align-items: center; justify-content: center; padding-top: 3px;
  }
  .btn-login {
    position: absolute; left: 750px; top: 0; height: 30px; padding-top: 3px;
    display: flex; align-items: center; font-size: 11px; font-weight: 600; color: var(--grey);
  }

  .main-nav {
    position: absolute; left: 0; top: 78px; width: 976px; height: 51px; background: var(--bar);
  }
  .nav-item {
    position: absolute; top: 0; height: 51px; display: flex; align-items: center; gap: 6px;
    font-family: "Oswald", "Arial Narrow", sans-serif; font-size: 15px; color: #fff;
  }
  .nav-item svg { display: block; }
  .nav-item.is-active { color: var(--green); }
  .nav-pointer {
    position: absolute; left: 216px; top: 45px; width: 0; height: 0;
    border-left: 5px solid transparent; border-right: 5px solid transparent;
    border-bottom: 6px solid var(--page);
  }
  .search-field {
    position: absolute; left: 622px; top: 97px; width: 150px; height: 13px;
    background: #fff; border: 1px solid #bbb;
    font-size: 6.5px; color: #b5b5b5; padding-left: 4px; line-height: 11px;
  }
  .search-btn {
    position: absolute; left: 775px; top: 97px; width: 18px; height: 13px; background: var(--green);
    display: flex; align-items: center; justify-content: center;
  }
  .search-advanced {
    position: absolute; left: 714px; top: 114px; font-size: 7px; color: #ddd; text-decoration: underline;
  }

  .video-item { position: absolute; left: 185px; width: 608px; height: 200px; }
  .video-thumb { position: absolute; left: 0; top: 0; width: 302px; height: 174px; }
  .play-btn {
    position: absolute; left: 137px; top: 72px; width: 29px; height: 29px; background: var(--green);
    display: flex; align-items: center; justify-content: center;
  }
  .comment-count { position: absolute; left: 0; top: 182px; }
  .rating { position: absolute; left: 210px; top: 183px; display: flex; gap: 6px; }
  .video-title {
    position: absolute; left: 321px; top: -2px; font-size: 13.4px; font-weight: 600; color: var(--ink);
  }
  .more-btn { position: absolute; left: 595px; top: 0; }
  .video-desc {
    position: absolute; left: 321px; top: 24px;
    font-size: 10.5px; line-height: 13.8px; color: var(--grey); white-space: nowrap;
  }
  .price-row { position: absolute; left: 326px; top: 146px; width: 282px; height: 28px; }
  .format {
    position: absolute; top: 0; width: 44px; height: 28px; background: var(--ink); color: #fff;
    font-size: 14px; font-weight: 600; display: flex; align-items: center; justify-content: center;
  }
  .price {
    position: absolute; top: 0; height: 28px; line-height: 28px;
    font-size: 18px; font-weight: 600; color: var(--green);
  }

  .pagination {
    position: absolute; left: 427px; top: 1062px; display: flex; align-items: center; gap: 6px;
    font-size: 12px; font-weight: 600; color: var(--grey);
  }
  .pagination .current { color: var(--green); }

  .site-footer {
    position: absolute; left: 0; top: 1092px; width: 976px; height: 108px; background: var(--footer);
  }
  .footer-links {
    position: absolute; top: 21px; width: 100%; text-align: center; font-size: 11.6px; color: #fff;
  }
  .social { position: absolute; left: 434px; top: 52px; display: flex; gap: 8px; }
  .social span { width: 22px; height: 22px; background: #fff; border-radius: 2px; }
</style>
</head>
<body>

<header class="site-header">
  <div class="brand"><span class="brand-mark"></span>Clipwerk B2B</div>
  <div class="btn-register">Anmelden</div>
  <div class="btn-login">Login</div>
</header>

<nav class="main-nav">
  <div class="nav-item is-active" style="left:185px">
    <svg width="14" height="26" viewBox="0 0 14 26"><path d="M4 0 L8 5 H5.5 V18 H2.5 V5 H0 Z M10 26 L14 21 H11.5 V8 H8.5 V21 H6 Z" fill="#60bb46"/></svg>
    Angebot
  </div>
  <div class="nav-item" style="left:281px">
    <svg width="18" height="14" viewBox="0 0 18 14"><g fill="#fff"><circle cx="2" cy="2" r="1.8"/><circle cx="2" cy="7" r="1.8"/><circle cx="2" cy="12" r="1.8"/><rect x="5" y="0.7" width="13" height="2.6"/><rect x="5" y="5.7" width="13" height="2.6"/><rect x="5" y="10.7" width="13" height="2.6"/></g></svg>
    Preise
  </div>
  <div class="nav-item" style="left:373px">
    <svg width="15" height="22" viewBox="0 0 15 22"><path d="M1 0 V22 H4 V14 L15 7 L4 0 Z" fill="#fff"/></svg>
    Über uns
  </div>
  <div class="nav-item" style="left:475px">
    <svg width="20" height="18" viewBox="0 0 20 18"><path d="M10 0 C15.5 0 20 3.5 20 8 C20 12.5 15.5 16 10 16 L4 18 L5 14 C2 12.5 0 10.4 0 8 C0 3.5 4.5 0 10 0 Z" fill="#fff"/><text x="10" y="12.5" text-anchor="middle" font-family="Arial, sans-serif" font-weight="700" font-size="11" fill="#262626">?</text></svg>
    FAQ
  </div>
  <div class="nav-item" style="left:553px">
    <svg width="7" height="22" viewBox="0 0 7 22"><rect x="1" y="0" width="5" height="15" rx="1.5" fill="#fff"/><path d="M1.5 17 H5.5 L3.5 21 Z" fill="#fff"/></svg>
    Blog
  </div>
  <div class="nav-pointer"></div>
</nav>
<div class="search-field">SUCHE</div>
<div class="search-btn"><svg width="8" height="8" viewBox="0 0 8 8"><circle cx="3" cy="3" r="2.1" fill="none" stroke="#fff" stroke-width="1.2"/><path d="M4.6 4.6 L7.4 7.4" stroke="#fff" stroke-width="1.4"/></svg></div>
<div class="search-advanced">erweiterte suche</div>

<svg width="0" height="0" style="position:absolute">
  <defs>
    <symbol id="star" viewBox="0 0 24 24"><path d="M12 1 L15 9 L23.5 9.2 L16.8 14.4 L19.2 22.8 L12 17.8 L4.8 22.8 L7.2 14.4 L0.5 9.2 L9 9 Z"/></symbol>
    <linearGradient id="half-star"><stop offset="50%" stop-color="#60bb46"/><stop offset="50%" stop-color="#d2d2d2"/></linearGradient>
    <symbol id="bubble" viewBox="0 0 18 18"><circle cx="9" cy="8" r="8" fill="#60bb46"/><path d="M13 13 L17 17 L10 15 Z" fill="#60bb46"/></symbol>
    <symbol id="plus" viewBox="0 0 14 14"><circle cx="7" cy="7" r="6.5" fill="#231f20"/><path d="M7 3.5 V10.5 M3.5 7 H10.5" stroke="#fff" stroke-width="2"/></symbol>
    <symbol id="play" viewBox="0 0 12 14"><path d="M0 0 L12 7 L0 14 Z" fill="#fff"/></symbol>
  </defs>
</svg>

<!-- Video 1 -->
<article class="video-item" style="top:155px">
  <div class="video-thumb" role="img" aria-label="Foto: Geschäftsleute besprechen Diagramme am Tisch" style="background:linear-gradient(135deg,#c9d2df,#eef0f3 55%,#b7b2aa)"></div>
  <div class="play-btn"><svg width="11" height="13"><use href="#play"/></svg></div>
  <div class="comment-count"><svg width="18" height="18"><use href="#bubble"/><text x="9" y="11" text-anchor="middle" font-family="Open Sans, sans-serif" font-size="7" font-weight="700" fill="#fff">42</text></svg></div>
  <div class="rating">
    <svg width="12" height="12" fill="#60bb46"><use href="#star"/></svg><svg width="12" height="12" fill="#60bb46"><use href="#star"/></svg><svg width="12" height="12" fill="#60bb46"><use href="#star"/></svg><svg width="12" height="12" fill="#60bb46"><use href="#star"/></svg><svg width="12" height="12" fill="#60bb46"><use href="#star"/></svg>
  </div>
  <h2 class="video-title">Marketing mit Video im Web</h2>
  <svg class="more-btn" width="13" height="13"><use href="#plus"/></svg>
  <p class="video-desc">Die Bildwerk Medienprojekte GmbH, Filmproduktion<br>und Videoproduktion für Werbefilm, Imagefilm,<br>Werbespot, Produktfilm aus Velmstadt bei Orrheim<br>in Westmark unterstützt die Bewegtbildtage Nord<br>als Mitveranstalter.</p>
  <div class="price-row">
    <div class="format" style="left:0">WEB</div><div class="price" style="left:50px">15 €</div>
    <div class="format" style="left:96px">SD</div><div class="price" style="left:146px">40 €</div>
    <div class="format" style="left:194px">HD</div><div class="price" style="left:245px">70 €</div>
  </div>
</article>

<!-- Video 2 -->
<article class="video-item" style="top:379px">
  <div class="video-thumb" role="img" aria-label="Foto: Ärzteteam in weißen Kitteln" style="background:linear-gradient(135deg,#f2f2f2,#dfe3e8 50%,#c8b9a4)"></div>
  <div class="play-btn"><svg width="11" height="13"><use href="#play"/></svg></div>
  <div class="comment-count"><svg width="18" height="18"><use href="#bubble"/><text x="9" y="11" text-anchor="middle" font-family="Open Sans, sans-serif" font-size="7" font-weight="700" fill="#fff">27</text></svg></div>
  <div class="rating">
    <svg width="12" height="12" fill="#60bb46"><use href="#star"/></svg><svg width="12" height="12" fill="#60bb46"><use href="#star"/></svg><svg width="12" height="12" fill="#60bb46"><use href="#star"/></svg><svg width="12" height="12" fill="url(#half-star)"><use href="#star"/></svg><svg width="12" height="12" fill="#d2d2d2"><use href="#star"/></svg>
  </div>
  <h2 class="video-title">Marketing mit Video im Web</h2>
  <svg class="more-btn" width="13" height="13"><use href="#plus"/></svg>
  <p class="video-desc">Die Bildwerk Medienprojekte GmbH, Filmproduktion<br>und Videoproduktion für Werbefilm, Imagefilm,<br>Werbespot, Produktfilm aus Velmstadt bei Orrheim<br>in Westmark unterstützt die Bewegtbildtage Nord<br>als Mitveranstalter.</p>
  <div class="price-row">
    <div class="format" style="left:0">WEB</div><div class="price" style="left:50px">9 €</div>
    <div class="format" style="left:96px">SD</div><div class="price" style="left:146px">29 €</div>
    <div class="format" style="left:194px">HD</div><div class="price" style="left:245px">54 €</div>
  </div>
</article>

<!-- Video 3 -->
<article class="video-item" style="top:603px">
  <div class="video-thumb" role="img" aria-label="Foto: Fröhliches Team legt die Hände zusammen" style="background:linear-gradient(135deg,#e9e6e1,#c8a68c 50%,#8c7f78)"></div>
  <div class="play-btn"><svg width="11" height="13"><use href="#play"/></svg></div>
  <div class="comment-count"><svg width="18" height="18"><use href="#bubble"/><text x="9" y="11" text-anchor="middle" font-family="Open Sans, sans-serif" font-size="7" font-weight="700" fill="#fff">12</text></svg></div>
  <div class="rating">
    <svg width="12" height="12" fill="#60bb46"><use href="#star"/></svg><svg width="12" height="12" fill="#60bb46"><use href="#star"/></svg><svg width="12" height="12" fill="#d2d2d2"><use href="#star"/></svg><svg width="12" height="12" fill="#d2d2d2"><use href="#star"/></svg><svg width="12" height="12" fill="#d2d2d2"><use href="#star"/></svg>
  </div>
  <h2 class="video-title">Marketing mit Video im Web</h2>
  <svg class="more-btn" width="13" height="13"><use href="#plus"/></svg>
  <p class="video-desc">Die Bildwerk Medienprojekte GmbH, Filmproduktion<br>und Videoproduktion für Werbefilm, Imagefilm,<br>Werbespot, Produktfilm aus Velmstadt bei Orrheim<br>in Westmark unterstützt die Bewegtbildtage Nord<br>als Mitveranstalter.</p>
  <div class="price-row">
    <div class="format" style="left:0">WEB</div><div class="price" style="left:50px">8 €</div>
    <div class="format" style="left:96px">SD</div><div class="price" style="left:146px">23 €</div>
    <div class="format" style="left:194px">HD</div><div class="price" style="left:245px">51 €</div>
  </div>
</article>

<!-- Video 4 -->
<article class="video-item" style="top:829px">
  <div class="video-thumb" role="img" aria-label="Foto: Studierende lesen in einer Bibliothek" style="background:linear-gradient(135deg,#9fb0c4,#c7a98a 45%,#e9e6e4 75%,#a36b4e)"></div>
  <div class="play-btn"><svg width="11" height="13"><use href="#play"/></svg></div>
  <div class="comment-count"><svg width="18" height="18"><use href="#bubble"/><text x="9" y="11" text-anchor="middle" font-family="Open Sans, sans-serif" font-size="7" font-weight="700" fill="#fff">84</text></svg></div>
  <div class="rating">
    <svg width="12" height="12" fill="#60bb46"><use href="#star"/></svg><svg width="12" height="12" fill="#60bb46"><use href="#star"/></svg><svg width="12" height="12" fill="#60bb46"><use href="#star"/></svg><svg width="12" height="12" fill="#60bb46"><use href="#star"/></svg><svg width="12" height="12" fill="#60bb46"><use href="#star"/></svg>
  </div>
  <h2 class="video-title">Marketing mit Video im Web</h2>
  <svg class="more-btn" width="13" height="13"><use href="#plus"/></svg>
  <p class="video-desc">Die Bildwerk Medienprojekte GmbH, Filmproduktion<br>und Videoproduktion für Werbefilm, Imagefilm,<br>Werbespot, Produktfilm aus Velmstadt bei Orrheim<br>in Westmark unterstützt die Bewegtbildtage Nord<br>als Mitveranstalter.</p>
  <div class="price-row">
    <div class="format" style="left:0">WEB</div><div class="price" style="left:50px">18 €</div>
    <div class="format" style="left:96px">SD</div><div class="price" style="left:146px">43 €</div>
    <div class="format" style="left:194px">HD</div><div class="price" style="left:245px">75 €</div>
  </div>
</article>

<div class="pagination">
  <svg width="6" height="9" viewBox="0 0 6 9"><path d="M6 0 V9 L0 4.5 Z" fill="#b5b5b5"/></svg>
  <span class="current">1</span><span>2</span><span>3</span><span>4</span><span>.....</span><span>32</span>
  <svg width="6" height="9" viewBox="0 0 6 9"><path d="M0 0 V9 L6 4.5 Z" fill="#60bb46"/></svg>
</div>

<footer class="site-footer">
  <div class="footer-links">Angebot | Preise | Über uns | FAQ | Blog | Kontakt</div>
  <div class="social"><span></span><span></span><span></span><span></span></div>
</footer>

</body>
</html>
```